Test and Tag business card design

We are an appliance test and tag company in Brisbane Australia requiring a business card design.
I don't have a logo.
Card front: Matte black background with white font.
Card back: White background with black font colour
Examples are attached
Minimalist design
Reason: Looking for more designs with an extreme minimal feel
Industry/Entity Type
Appliance
Contact Information for Business Card
Business name: Harbor Check and Label
Description: Onsite Electrical Testing and Tagging
Licence No. 41853
Name: Greg Pellow
Mobile: 0418 526 937
Email: greg@harborcheckandlabel.com.au
Web: harborcheckandlabel.com.au
Logo Text
Harbor Check and Label
Look and feel

```html
<!DOCTYPE html>
<html lang="en">
<head>
<meta charset="utf-8">
<title>Harbor Check and Label – Business Card</title>
<link rel="stylesheet" href="https://fonts.googleapis.com/css2?family=Arimo:ital,wght@0,400;0,700;1,400&display=swap">
<style>
  :root {
    --page: #ffffff;
    --card-dark: #2a2627;
    --card-light: #ffffff;
    --ink-light: #ffffff;
    --ink-dark: #231f20;
    --edge: #d9d9d9;
  }
  * { margin: 0; padding: 0; box-sizing: border-box; }
  html, body {
    width: 1200px; height: 900px; overflow: hidden;
    background: var(--page);
    font-family: "Arimo", Arial, sans-serif;
  }
  .canvas { position: relative; width: 1200px; height: 900px; }

  .card {
    position: absolute; left: 330px; width: 540px; height: 311px;
  }
  .card--front { top: 37px; background: var(--card-dark); color: var(--ink-light); }
  .card--back { top: 430px; background: var(--card-light); color: var(--ink-dark); border: 1px solid var(--edge); }

  .brand-name {
    position: absolute; left: 60px; top: 92px; width: 200px;
    font-weight: 700; font-size: 26px; line-height: 1.05; letter-spacing: 0.5px;
    text-transform: uppercase;
  }
  .person-name {
    position: absolute; left: 316px; top: 80px;
    font-size: 26px; font-weight: 400;
  }
  .contact-list {
    position: absolute; left: 267px; top: 136px; list-style: none;
  }
  .contact-item {
    display: flex; align-items: center; gap: 7px;
    height: 30px; font-size: 15px;
  }
  .contact-icon { width: 16px; height: 16px; fill: currentColor; flex: none; }
  .tagline {
    position: absolute; left: 0; right: 0; top: 239px; text-align: center;
    font-size: 14px;
  }
  .tagline .licence { font-style: italic; }
</style>
</head>
<body>
<main class="canvas">

  <section class="card card--front" aria-label="Business card front">
    <div class="brand-name">Harbor Check and Label</div>
    <h1 class="person-name">Greg Pellow</h1>
    <ul class="contact-list">
      <li class="contact-item">
        <svg class="contact-icon" viewBox="0 0 16 16" aria-hidden="true"><path d="M1 5c0-2 3-3 7-3s7 1 7 3v1.5h-3.5V5h-7v1.5H1z"/><path d="M3 7.5h10l1 6.5H2zM8 9a2 2 0 1 0 0.01 0z"/></svg>
        <span>0418 526 937</span>
      </li>
      <li class="contact-item">
        <svg class="contact-icon" viewBox="0 0 16 16" aria-hidden="true"><path d="M1 3h14v10H1zM2.5 4.5v0.4L8 9l5.5-4.1v-0.4zM2.5 6.7v4.8h11V6.7L8 10.8z"/></svg>
        <span>greg@harborcheckandlabel.com.au</span>
      </li>
      <li class="contact-item">
        <svg class="contact-icon" viewBox="0 0 16 16" aria-hidden="true"><circle cx="8" cy="8" r="7.5"/><rect x="7" y="6.5" width="2" height="6" fill="var(--card-dark)"/><circle cx="8" cy="4.3" r="1.1" fill="var(--card-dark)"/></svg>
        <span>harborcheckandlabel.com.au</span>
      </li>
    </ul>
    <p class="tagline">Onsite Electrical Testing and Tagging - <span class="licence">Licence No. 41853</span></p>
  </section>

  <section class="card card--back" aria-label="Business card back">
    <div class="brand-name">Harbor Check and Label</div>
    <h2 class="person-name">Greg Pellow</h2>
    <ul class="contact-list">
      <li class="contact-item">
        <svg class="contact-icon" viewBox="0 0 16 16" aria-hidden="true"><path d="M1 5c0-2 3-3 7-3s7 1 7 3v1.5h-3.5V5h-7v1.5H1z"/><path d="M3 7.5h10l1 6.5H2zM8 9a2 2 0 1 0 0.01 0z"/></svg>
        <span>0418 526 937</span>
      </li>
      <li class="contact-item">
        <svg class="contact-icon" viewBox="0 0 16 16" aria-hidden="true"><path d="M1 3h14v10H1zM2.5 4.5v0.4L8 9l5.5-4.1v-0.4zM2.5 6.7v4.8h11V6.7L8 10.8z"/></svg>
        <span>greg@harborcheckandlabel.com.au</span>
      </li>
      <li class="contact-item">
        <svg class="contact-icon" viewBox="0 0 16 16" aria-hidden="true"><circle cx="8" cy="8" r="7.5"/><rect x="7" y="6.5" width="2" height="6" fill="var(--card-light)"/><circle cx="8" cy="4.3" r="1.1" fill="var(--card-light)"/></svg>
        <span>harborcheckandlabel.com.au</span>
      </li>
    </ul>
    <p class="tagline">Onsite Electrical Testing and Tagging - <span class="licence">Licence No. 41853</span></p>
  </section>

</main>
</body>
</html>
```